Graphic / Web page design for Pale Harbor Game Studios - Quillfang

This will become a site for a game design studio. The primary game that we will be focusing on is Quillfang.

If you are a graphic artist and web design is really not your thing I'm still open to you designing the graphic look for the website. I can if required, slice the site and make it into a template for wordpress. I want a slick look that really shows off Pale Harbor Game Studios

You can see the current website the chosen design will replace and the trailer for the game at Quillfang.example

NOTICE: I'm not looking for a template with a picture from my existing website plugged in. I've got access to many templates and I can plug in pictures. I will select the designer that gives me a nice looking Pale Harbor Game Studios look.

All the artwork needs to be original. I will be adding a developer blog to the website but otherwise it only needs to be a few pages to showcase the studio and our first game, Quillfang.

The site that needs re-design with a new fresh look for what a quality game studio website should look like.

The ideal candidate would be able to have it ready to host in WordPress or another CMS that is easy to setup.

I'm not specifying a lot of detail in regards to fonts or colors.

Many thanks for the consideration.

Target Market(s)

Video gamers.

Number of Pages Required

3 page

Requirements
Must have
• I need a real eye catching home page that has the qualities that you would expect for a professional game studio. As we produce games, we will add pages to the site to showcase each of our new games.
• I'll have a blog page that I can discuss new releases to the game as well as a contact page.
Nice to have
• While this is a site for a video game studio, our first and primary game we will be focusing on for the next six months will be Quillfang. Therefore we want the homepage to showcase Quillfang and make it the center of attention for this version of the website. A nice to have would be a balance that we still are 'Pale Harbor Game Studios'.

```html
<!DOCTYPE html>
<html lang="en">
<head>
<meta charset="utf-8">
<title>Quillfang — Pale Harbor Game Studios</title>
<link rel="stylesheet" href="https://fonts.googleapis.com/css2?family=Oswald:wght@400;500;700&family=Raleway:wght@400;600;700&display=swap">
<style>
  :root {
    --red: #d11a1a;
    --ink: #0b0b0d;
    --panel: #141416;
    --navy: #10202c;
    --white: #ffffff;
  }
  * { box-sizing: border-box; margin: 0; padding: 0; }
  html, body { width: 1200px; height: 3122px; overflow: hidden; }
  body { position: relative; background: var(--ink); color: var(--white); font-family: "Raleway", sans-serif; }
  .abs { position: absolute; }

  /* HERO */
  .hero { position: absolute; left: 0; top: 0; width: 1200px; height: 924px; overflow: hidden;
    background: radial-gradient(ellipse 360px 420px at 600px 330px, #6e3934 0%, #352a31 45%, transparent 75%),
                linear-gradient(180deg, #16303e 0%, var(--navy) 60%, #0c1820 100%); }
  .hero-art { position: absolute; left: 0; top: 0; width: 1200px; height: 924px; }
  .hero-glow { position: absolute; left: 300px; top: 560px; width: 600px; height: 260px;
    background: radial-gradient(ellipse 300px 130px at 50% 50%, rgba(40,42,48,0.85) 0%, rgba(20,22,28,0.5) 55%, transparent 100%); }
  .brand { position: absolute; left: 128px; top: 34px; display: flex; align-items: center; gap: 16px; }
  .brand-dot { width: 50px; height: 50px; border-radius: 50%; border: 3px solid var(--white); }
  .brand-name { font-family: "Oswald", sans-serif; font-weight: 500; font-size: 26px; line-height: 1; letter-spacing: 0.5px; text-transform: uppercase; color: var(--white); }
  .main-nav { position: absolute; left: 536px; top: 38px; display: flex; align-items: center; gap: 28px; font-size: 16px; font-weight: 600; }
  .main-nav a { color: var(--white); text-decoration: none; }
  .main-nav .is-active { background: var(--red); padding: 14px 20px; }
  .hero-kicker { position: absolute; left: 0; width: 1200px; top: 228px; text-align: center; font-family: "Oswald", sans-serif; font-size: 56px; color: var(--red); letter-spacing: 1px; }
  .hero-title { position: absolute; left: 0; width: 1200px; top: 280px; text-align: center; font-family: "Oswald", sans-serif; font-weight: 700; font-size: 132px; line-height: 1; letter-spacing: 2px; }
  .btn-outline-red { position: absolute; left: 530px; top: 468px; width: 140px; height: 44px; border: 2px solid var(--red); color: var(--red); font-size: 15px; font-weight: 700; display: flex; align-items: center; justify-content: center; text-transform: uppercase; }
  .hero-curve { position: absolute; left: 0; top: 720px; }
  .scroll-down { position: absolute; left: 574px; top: 846px; width: 52px; height: 52px; border-radius: 50%; border: 2px solid #cfcfcf; background: var(--white); }

  .dots { position: absolute; display: flex; flex-direction: column; gap: 14px; }
  .dots span { width: 14px; height: 14px; border-radius: 50%; background: var(--white); }
  .dots .on { background: transparent; border: 2px solid var(--white); }

  /* INTRO */
  .intro-art { position: absolute; left: 0; top: 924px; width: 569px; height: 698px;
    background: radial-gradient(ellipse 220px 300px at 300px 360px, #6b3a3c 0%, #2a3440 55%, transparent 85%), linear-gradient(180deg, #1d3a48, #0f1f28); }
  .intro-panel { position: absolute; left: 569px; top: 924px; width: 631px; height: 698px; background: linear-gradient(180deg, var(--panel) 0%, #0e0e10 100%); }
  .section-title { font-family: "Oswald", sans-serif; font-weight: 700; text-transform: uppercase; line-height: 1; }
  .intro-title { position: absolute; left: 52px; top: 70px; font-size: 68px; color: var(--red); }
  .intro-sub { position: absolute; left: 52px; top: 150px; font-size: 17px; font-weight: 600; text-transform: uppercase; }
  .trailer { position: absolute; left: 52px; top: 193px; width: 490px; height: 280px;
    background: radial-gradient(ellipse 70px 120px at 240px 150px, #6b6f85 0%, transparent 100%), linear-gradient(180deg, #4f6a7c 0%, #2c3d4a 60%, #1a232b 100%); }
  .intro-soon { position: absolute; left: 52px; top: 494px; font-size: 26px; }
  .intro-copy { position: absolute; left: 52px; top: 534px; width: 490px; font-size: 14px; line-height: 1.5; color: #d7d7da; }

  /* FEATURE */
  .feature-panel { position: absolute; left: 0; top: 1622px; width: 628px; height: 716px; background: linear-gradient(180deg, #141416 0%, #202023 100%); }
  .feature-title { position: absolute; left: 126px; top: 140px; font-size: 62px; }
  .feature-copy { position: absolute; left: 126px; top: 222px; width: 430px; font-size: 20px; line-height: 1.42; color: #e6e6e8; }
  .btn { position: absolute; top: 513px; height: 58px; display: flex; align-items: center; justify-content: center; font-size: 18px; text-transform: uppercase; }
  .btn-ghost { left: 126px; width: 180px; border: 2px solid #bdbdbd; }
  .btn-red { left: 320px; width: 180px; background: var(--red); }
  .feature-art { position: absolute; left: 628px; top: 1622px; width: 572px; height: 716px;
    background: radial-gradient(ellipse 230px 200px at 300px 400px, #ffb24a 0%, #e0501e 35%, #5a2a20 65%, transparent 90%), linear-gradient(180deg, #20303a 0%, #151c22 100%); }

  /* CONTACT */
  .contact { position: absolute; left: 0; top: 2338px; width: 1200px; height: 784px; background: #050506; }
  .contact-map { position: absolute; left: 0; top: 0; width: 1200px; height: 560px;
    background: radial-gradient(ellipse 520px 250px at 600px 260px, #1f1f22 0%, #0c0c0e 70%, transparent 100%); }
  .contact-title { position: absolute; left: 216px; top: 58px; font-size: 104px; }
  .contact-title em { font-style: normal; color: var(--red); }
  .contact-info { position: absolute; left: 816px; top: 64px; display: flex; flex-direction: column; gap: 14px; font-size: 17px; }
  .contact-info li { list-style: none; display: flex; align-items: center; gap: 14px; }
  .contact-info .ico { width: 24px; height: 24px; border-radius: 50%; background: var(--red); display: flex; align-items: center; justify-content: center; }
  .field { position: absolute; background: var(--white); color: #777; font-size: 16px; padding: 12px 14px; }
  .f-name { left: 216px; top: 244px; width: 384px; height: 58px; }
  .f-mail { left: 216px; top: 324px; width: 384px; height: 58px; }
  .f-enquiry { left: 621px; top: 244px; width: 384px; height: 138px; }
  .send { position: absolute; left: 785px; top: 404px; width: 98px; height: 48px; background: var(--red); display: flex; align-items: center; justify-content: center; font-size: 17px; font-weight: 700; text-transform: uppercase; }
  .reset { position: absolute; left: 897px; top: 404px; width: 108px; height: 48px; background: #2a2a2d; display: flex; align-items: center; justify-content: center; font-size: 17px; font-weight: 700; text-transform: uppercase; }
  .social { position: absolute; left: 0; width: 1200px; top: 524px; display: flex; justify-content: center; gap: 20px; }
  .social span { width: 40px; height: 40px; border-radius: 50%; background: var(--white); }
  .social span:first-child { background: var(--red); }
  .footer-nav { position: absolute; left: 0; width: 1200px; top: 602px; display: flex; justify-content: center; gap: 46px; font-size: 13px; font-weight: 600; text-transform: uppercase; }
  .footer-nav .is-active { color: var(--red); }
  .copyright { position: absolute; left: 0; width: 1200px; top: 656px; text-align: center; font-size: 18px; text-transform: uppercase; }
  .legal-bar { position: absolute; left: 0; top: 714px; width: 1200px; height: 70px; border-top: 1px solid #1e1e21; }
  .legal { position: absolute; right: 120px; top: 24px; font-size: 13px; text-transform: uppercase; }
  .legal em { font-style: normal; color: var(--red); }
</style>
</head>
<body>

<header class="hero">
  <div class="hero-art" role="img" aria-label="Hooded spell-caster character artwork in dark blue and crimson tones"></div>
  <svg class="hero-curve" width="1200" height="204" viewBox="0 0 1200 204" aria-hidden="true">
    <path d="M0 204 C 180 60, 420 10, 600 10 C 780 10, 1020 60, 1200 204 Z" fill="#ffffff"/>
  </svg>
  <div class="hero-glow" role="img" aria-label="Game hardware product shot"></div>
  <div class="brand"><span class="brand-dot"></span><span class="brand-name">Pale Harbor Game Studios</span></div>
  <nav class="main-nav">
    <a class="is-active" href="#">Quillfang</a>
    <a href="#">About The Game</a>
    <a href="#">Cortexa's ThoughtBand</a>
    <a href="#">Pre Order Now</a>
  </nav>
  <p class="hero-kicker">WELCOME TO</p>
  <h1 class="hero-title">QUILLFANG</h1>
  <a class="btn-outline-red">Read More</a>
  <div class="scroll-down">
    <svg width="48" height="48" viewBox="0 0 48 48" aria-hidden="true"><path d="M24 15 V31 M18 25 L24 31 L30 25" stroke="#d11a1a" stroke-width="2.5" fill="none"/></svg>
  </div>
  <div class="dots" style="left:1130px;top:312px;"><span class="on"></span><span></span><span></span><span></span></div>
</header>

<section>
  <div class="intro-art" role="img" aria-label="Close-up of the hooded mage character in red robes"></div>
  <div class="intro-panel">
    <h2 class="section-title intro-title">QUILLFANG</h2>
    <p class="intro-sub">Quillfang - Learn spells using only your mind!</p>
    <div class="trailer" role="img" aria-label="Gameplay trailer still showing a spell duel in an arena"></div>
    <h3 class="section-title intro-soon">Coming Soon!</h3>
    <p class="intro-copy">Pale Harbor Game Studios presents Quillfang, a game that combines exciting spell-casting duels, gorgeous imagery, and cutting-edge biosensor technology. Using Cortexa's ThoughtBand - a research-grade wireless EEG headset - you'll learn to harness the power of your own mind to build an arsenal of powerful spells and defeat your opponent.</p>
  </div>
  <div class="dots" style="left:1130px;top:1200px;"><span></span><span class="on"></span><span></span><span></span></div>
</section>

<section>
  <div class="feature-panel">
    <h2 class="section-title feature-title">COMING SOON</h2>
    <p class="feature-copy">Pale Harbor Game Studios presents Quillfang, a game that combines exciting spell-casting duels, gorgeous imagery, and cutting-edge biosensor technology. Using Cortexa's ThoughtBand - a research-grade wireless EEG headset - you'll learn to harness the power of your own mind to build an arsenal of powerful spells and defeat your opponent.</p>
    <a class="btn btn-ghost">Read More</a>
    <a class="btn btn-red">Get Started</a>
  </div>
  <div class="feature-art" role="img" aria-label="Mage standing on stone steps before a blazing fire spell"></div>
  <div class="dots" style="left:1130px;top:1900px;"><span></span><span></span><span class="on"></span><span></span></div>
</section>

<footer class="contact">
  <div class="contact-map" role="img" aria-label="Faint dotted world map backdrop"></div>
  <h2 class="section-title contact-title">CONTACT <em>US</em></h2>
  <ul class="contact-info">
    <li><span class="ico"><svg width="14" height="10" viewBox="0 0 14 10" aria-hidden="true"><rect x="0.5" y="0.5" width="13" height="9" fill="none" stroke="#fff"/><path d="M0.5 0.5 L7 6 L13.5 0.5" fill="none" stroke="#fff"/></svg></span>sales@Quillfang.example</li>
    <li><span class="ico"><svg width="12" height="12" viewBox="0 0 12 12" aria-hidden="true"><path d="M2 1 L4.5 1 L5.5 4 L4 5 C5 7 6 8 7.5 8.5 L8.5 7 L11 8 L11 10.5 C6 11 1 6 2 1 Z" fill="#fff"/></svg></span>555 0142</li>
    <li><span class="ico"><svg width="12" height="12" viewBox="0 0 12 12" aria-hidden="true"><path d="M2 1 L4.5 1 L5.5 4 L4 5 C5 7 6 8 7.5 8.5 L8.5 7 L11 8 L11 10.5 C6 11 1 6 2 1 Z" fill="#fff"/></svg></span>555 0187</li>
  </ul>
  <div class="field f-name">First Name :</div>
  <div class="field f-mail">E-Mail :</div>
  <div class="field f-enquiry">Enquiry :</div>
  <div class="send">Send</div>
  <div class="reset">Reset</div>
  <div class="social"><span></span><span></span><span></span><span></span><span></span></div>
  <nav class="footer-nav">
    <span class="is-active">Quillfang</span><span>About The Game</span><span>Cortexa ThoughtBand</span><span>Pre-Order Now</span>
  </nav>
  <p class="copyright">Copyright © 2015. All rights reserved.</p>
  <div class="legal-bar"><p class="legal">Privacy Policy &amp; <em>Terms of Use</em></p></div>
</footer>

</body>
</html>
```